812 EDDM FLYER FOR CARPET CLEANING & WINDOW WASHING

Full Size Double Sided full color EDDM mailer

****PLEASE MAKE FONT TYPE, SIZE, COLOR, SPACING SAME AS IS EXAMPLE FLYER*******

***I have uploaded LOGO... It is on the VAN WRAP 812 CLEANING & RESTORATION

I have included an EDDM flyer and want my flyer to look like the example I uploaded.

I wanted to make it look Better & add my images and content. I have included the content under Must Haves......

Raindrop background

****Not all images will be used. Each service requires 2 images as seen on examply flyer... Please pic best 2 for each service, I can purchase new stock photo if needed

Target Market(s)

Residential Home Owners

Industry/Entity Type

Cleaning Service

Font styles to use
Serif

Colors
0555a3
ec1f27
fbed22
ffc214

Requirements
Must have
• Look Like Example EDDM postcard uploaded
• My images & content
• CARPET CLEANING Safe Eco-Friendly Truck Mounted Steam Cleaning. Say goodbye to those ugly carpet stains.
• WINDOW WASHING Interior/Exterior & Screens. Crystal Clear & Streak Free Windows
• POWER WASHING: Soft Wash & Power Wash. Safely cleans
• WATER DAMAGE: Got Mold or Water damage? Free IR Imaging Detection
• TILE & GROUT: Clean, Restore & Rejuvenate Tile, Grout & Stone
• MAINTENANCE: Professional & dependable repairs. We can Fit It!
• Call Today! 858-555-0147
• www.TidyNorth812.example
• ECO FRIENDLY CLEANING
• San Diego’s Trusted Cleaning Specialists

```html
<!DOCTYPE html>
<html lang="en">
<head>
<meta charset="utf-8">
<title>812 Cleaning &amp; Restoration – EDDM Mailer</title>
<link href="https://fonts.googleapis.com/css2?family=Archivo:wght@800&family=Fira+Sans+Condensed:ital,wght@0,400;0,600;1,700&family=Arimo:wght@700&display=swap" rel="stylesheet">
<style>
  :root{
    --brand-blue:#0555a3;
    --deep-blue:#1a3f9a;
    --sky-blue:#1f8fe0;
    --bright-blue:#3aa8f0;
    --red:#ec1f27;
    --yellow:#fbed22;
    --gold:#ffc214;
    --white:#ffffff;
    --ink:#1b1b1b;
    --page:#e4e6ea;
  }
  *{box-sizing:border-box;margin:0;padding:0}
  html,body{width:1200px;height:1200px;overflow:hidden}
  body{background:var(--page);position:relative;font-family:"Fira Sans Condensed",sans-serif}

  .mailer{position:absolute;width:592px;height:483px;overflow:hidden;
    background:linear-gradient(180deg,var(--sky-blue) 0%,var(--bright-blue) 55%,#1d7fd6 100%);
    box-shadow:0 6px 18px rgba(0,0,0,.35)}
  .mailer--front{left:312px;top:100px}
  .mailer--back{left:297px;top:645px}

  .headline-band{position:absolute;left:0;top:0;height:148px;width:100%;
    background:linear-gradient(180deg,#1c4fb4 0%,var(--deep-blue) 45%,#2767c9 100%)}
  .headline-band::after{content:"";position:absolute;left:0;right:0;top:28px;height:2px;background:rgba(255,255,255,.55)}
  .headline-band .rule-bottom{position:absolute;left:0;right:0;bottom:0;height:2px;background:rgba(255,255,255,.55)}

  .pill{position:absolute;background:var(--yellow);border:2px solid var(--deep-blue);border-radius:40px;
    display:flex;align-items:center;justify-content:center;color:var(--deep-blue);
    font-family:"Fira Sans Condensed",sans-serif;font-style:italic;font-weight:700;white-space:nowrap}
  .main-title{position:absolute;color:var(--white);font-family:"Archivo",sans-serif;font-weight:800;
    white-space:nowrap;letter-spacing:.5px;line-height:1}

  /* front */
  .photo-grid{position:absolute;left:19px;top:166px;width:557px;height:240px;display:grid;
    grid-template-columns:repeat(3,1fr);grid-template-rows:repeat(2,1fr);gap:2px;
    background:var(--white);border:2px solid var(--white);border-radius:8px;overflow:hidden}
  .photo-tile{position:relative}
  .photo-tile .caption{position:absolute;left:0;right:0;bottom:0;height:30px;
    background:linear-gradient(180deg,rgba(255,255,255,0),rgba(255,255,255,.85));
    display:flex;align-items:flex-end;justify-content:center;padding-bottom:4px;
    color:var(--deep-blue);font-weight:600;font-size:15px}
  .photo{position:absolute;inset:0}

  .brand{position:absolute;display:flex;align-items:center;gap:8px;color:var(--white);
    font-family:"Fira Sans Condensed",sans-serif;font-weight:600;font-size:16px;line-height:1.1}
  .brand .dot{width:28px;height:28px;border-radius:50%;background:var(--gold);flex:none}

  .contact{position:absolute;text-align:center;color:var(--white);font-family:"Fira Sans Condensed",sans-serif;line-height:1.08;white-space:nowrap}
  .contact .phone{font-weight:400;font-size:27px}
  .contact .web{font-weight:600;font-size:19px}
  .contact .tagline{font-weight:600;font-size:11.5px}

  .back-tab{position:absolute;left:482px;top:418px;width:92px;height:54px;background:var(--yellow);
    clip-path:polygon(0 0,82% 0,100% 50%,82% 100%,0 100%);
    color:var(--deep-blue);font-style:italic;font-weight:700;font-size:10.5px;line-height:1.25;
    padding:7px 0 0 12px}

  /* back */
  .address-block{position:absolute;left:372px;top:0;width:220px;height:149px;background:var(--white);
    font-family:"Arimo",sans-serif;color:var(--ink)}
  .indicia{position:absolute;left:142px;top:17px;width:58px;height:50px;border:1.5px solid #333;
    font-size:7px;line-height:1.2;text-align:center;padding-top:3px;font-weight:400}
  .indicia b{font-size:8.5px}
  .ecrwss{position:absolute;left:54px;top:81px;font-size:10px}
  .recipient{position:absolute;left:27px;top:101px;font-size:11px;line-height:1.2}

  .service-panel{position:absolute;left:20px;top:170px;width:551px;height:218px;background:var(--white);
    border-radius:10px;overflow:hidden}
  .service-photo{position:absolute}
  .service-copy{position:absolute;width:84px}
  .service-copy h3{color:var(--red);font-weight:600;font-size:13.5px;line-height:1.1;text-transform:uppercase;margin-bottom:6px}
  .service-copy p{font-size:7.6px;line-height:1.3;color:var(--ink)}
  .service-copy--right{text-align:right}

  .eco-line{position:absolute;left:28px;top:452px;color:var(--white);font-family:"Arimo",sans-serif;
    font-weight:700;font-size:13px;letter-spacing:.6px}
  .badge{position:absolute;background:var(--white)}
  .badge--round{left:509px;top:394px;width:34px;height:34px;border-radius:50%;border:3px solid #2fa56a}
  .badge--rect{left:502px;top:437px;width:55px;height:21px;border:2px solid var(--white);background:#173a7a}
</style>
</head>
<body>

<!-- FRONT -->
<section class="mailer mailer--front">
  <div class="headline-band"><span class="rule-bottom"></span></div>
  <div class="pill" style="left:120px;top:14px;width:354px;height:34px;font-size:24px">Don’t Miss Out! We’re offering:</div>
  <div class="main-title" style="left:0;width:592px;text-align:center;top:72px;font-size:57px">FREE ESTIMATES</div>
  <div class="pill" style="left:138px;top:134px;width:316px;height:37px;font-size:28px">On All of Our Services!</div>

  <div class="photo-grid">
    <div class="photo-tile"><div class="photo" role="img" aria-label="Technician steam cleaning carpet in an empty room" style="background:linear-gradient(160deg,#e8ecef,#b9c3cc)"></div><span class="caption">Carpet Cleaning</span></div>
    <div class="photo-tile"><div class="photo" role="img" aria-label="Worker squeegeeing a large window" style="background:linear-gradient(160deg,#dfe6ec,#8aa3bd)"></div><span class="caption">Window Washing</span></div>
    <div class="photo-tile"><div class="photo" role="img" aria-label="Pressure washer cleaning a brick patio" style="background:linear-gradient(160deg,#a86a62,#6f3f3b)"></div><span class="caption">Power Washing</span></div>
    <div class="photo-tile"><div class="photo" role="img" aria-label="Homeowner looking at a leaking pipe" style="background:linear-gradient(160deg,#c9ced3,#8c7866)"></div><span class="caption">Water Damage</span></div>
    <div class="photo-tile"><div class="photo" role="img" aria-label="Technician cleaning a tile floor" style="background:linear-gradient(160deg,#e6dccc,#a89578)"></div><span class="caption">Tile &amp; Grout</span></div>
    <div class="photo-tile"><div class="photo" role="img" aria-label="Maintenance technician writing on a clipboard" style="background:linear-gradient(160deg,#cfd6de,#2e3f66)"></div><span class="caption">Maintenance</span></div>
  </div>

  <div class="brand" style="left:36px;top:422px;width:190px"><span class="dot"></span><span>812 CLEANING<br>&amp; RESTORATION</span></div>
  <div class="contact" style="left:228px;top:414px;width:250px">
    <div class="phone">(858) 555-0147</div>
    <div class="web">www.TidyNorth812.example</div>
    <div class="tagline">San Diego’s Trusted Cleaning Specialists</div>
  </div>
  <div class="back-tab">Look on back<br>to see what we<br>can do for you!</div>
</section>

<!-- BACK -->
<section class="mailer mailer--back">
  <div class="headline-band" style="width:372px"><span class="rule-bottom"></span></div>
  <div class="pill" style="left:15px;top:13px;width:334px;height:33px;font-size:23px">Don’t Miss Out! We’re offering:</div>
  <div class="main-title" style="left:16px;top:71px;font-size:37px">FREE ESTIMATES</div>
  <div class="pill" style="left:13px;top:126px;width:337px;height:40px;font-size:28px">On All of Our Services!</div>

  <div class="address-block">
    <div class="indicia">PRST STD<br>ECRWSS<br>U.S. POSTAGE<br><b>PAID</b><br>EDDM Retail</div>
    <div class="ecrwss">********ECRWSS********</div>
    <div class="recipient">Local<br>Postal Customer</div>
  </div>

  <div class="service-panel">
    <div class="service-photo" role="img" aria-label="Technician cleaning outside a home" style="left:4px;top:14px;width:82px;height:100px;background:linear-gradient(160deg,#6f8a5a,#3c4a38)"></div>
    <div class="service-copy" style="left:98px;top:22px"><h3>Carpet<br>Cleaning</h3><p>Safe Eco-Friendly Truck Mounted Steam Cleaning. Say goodbye to those ugly carpet stains.</p></div>

    <div class="service-photo" role="img" aria-label="Squeegee on a window with ocean view" style="left:182px;top:12px;width:91px;height:100px;background:linear-gradient(180deg,#4a8fd0,#8fb0c8 60%,#3a3a3a)"></div>
    <div class="service-copy" style="left:280px;top:22px"><h3>Window<br>Washing</h3><p>Interior/Exterior &amp; Screens. Crystal Clear &amp; Streak Free Windows</p></div>

    <div class="service-photo" role="img" aria-label="Worker washing a clay tile roof" style="left:367px;top:0;width:91px;height:110px;background:linear-gradient(160deg,#d0653a,#8a3b20)"></div>
    <div class="service-copy" style="left:467px;top:22px"><h3>Power<br>Washing</h3><p>Soft Wash &amp; Power Wash. Safely cleans</p></div>

    <div class="service-copy service-copy--right" style="left:2px;top:130px"><h3>Water<br>Damage</h3><p>Got Mold or Water damage? Free IR Imaging Detection</p></div>
    <div class="service-photo" role="img" aria-label="Technician inspecting a water-damaged ceiling" style="left:92px;top:114px;width:90px;height:104px;background:linear-gradient(160deg,#d8d4cc,#6b5a48)"></div>

    <div class="service-copy service-copy--right" style="left:184px;top:132px"><h3>Tile &amp;<br>Grout</h3><p>Clean, Restore &amp; Rejuvenate Tile, Grout &amp; Stone</p></div>
    <div class="service-photo" role="img" aria-label="Rotary cleaner on a stone tile floor" style="left:273px;top:114px;width:92px;height:104px;background:linear-gradient(160deg,#a9a9a6,#6a6a68)"></div>

    <div class="service-copy service-copy--right" style="left:367px;top:132px"><h3>Maintenance</h3><p>Professional &amp; dependable repairs. We can Fit It!</p></div>
    <div class="service-photo" role="img" aria-label="Technician in hard hat repairing equipment" style="left:457px;top:114px;width:94px;height:104px;background:linear-gradient(160deg,#c9d6e4,#23417e)"></div>
  </div>

  <div class="brand" style="left:32px;top:404px;width:190px"><span class="dot"></span><span>812 CLEANING<br>&amp; RESTORATION</span></div>
  <div class="eco-line">ECO FRIENDLY CLEANING</div>
  <div class="contact" style="left:232px;top:398px;width:250px">
    <div class="phone">(858) 555-0147</div>
    <div class="web">www.TidyNorth812.example</div>
    <div class="tagline">San Diego’s Trusted Cleaning Specialists</div>
  </div>
  <div class="badge badge--round" role="img" aria-label="Eco certification badge"></div>
  <div class="badge badge--rect" role="img" aria-label="Industry certification badge"></div>
</section>

</body>
</html>
```